Warranty Card Design for Mattress Brand

We would like to design a warranty card for our mattresses,
it consists of 2 pages in one card (front and back) to be neatly showing our warranty details/text , our logo , our website, address and telephone clearly.

Target Market(s)

household

Font styles to use
Serif
Script

Colors
3277b5
33a6d7
85cae6
0492cd
3176b5
0355a3
85abd2
cee9f5
85acd3

Requirements
Must have
• a nice warranty logo
Nice to have
• a nice warranty logo with a neat text and clear layout, colors have to be related to the logo

```html
<!DOCTYPE html>
<html lang="en">
<head>
<meta charset="utf-8">
<title>Slumberwell Warranty Card</title>
<link href="https://fonts.googleapis.com/css2?family=Montserrat:wght@400;500;600&display=swap" rel="stylesheet">
<style>
:root{
  --ink:#111;
  --brand:#4a72c8;
  --blue-deep:#3a66e0;
  --blue-mid:#6f95ee;
  --blue-soft:#c9d8f8;
  --blue-mist:#eaf0fc;
  --seal:#7b7fd0;
  --rule:#9a9a9a;
  --board-a:#c6d4f4;
  --board-b:#8893b0;
  --right-bg:#ffffff;
}
*{margin:0;padding:0;box-sizing:border-box}
html,body{width:1200px;height:546px;overflow:hidden;background:#fff}
body{position:relative;font-family:"Montserrat",sans-serif;color:var(--ink)}
.board{position:absolute;left:8px;top:8px;width:750px;height:530px;border-radius:8px;
  background:linear-gradient(135deg,var(--board-a) 0%,#aebbe0 50%,var(--board-b) 100%)}
.sheet{position:absolute;top:50px;width:318px;height:452px;background:linear-gradient(180deg,#fff 60%,var(--blue-mist) 100%);
  box-shadow:0 2px 8px rgba(30,40,80,.35);overflow:hidden}
.sheet--front{left:50px}
.sheet--back{left:402px}
.swoosh{position:absolute;top:0;right:0}
.fade{position:absolute;left:0;bottom:0}
.brand-name{position:absolute;font-weight:400;color:var(--brand);letter-spacing:.5px}
.sheet .brand-name{left:10px;top:22px;font-size:24px}
.el{position:absolute;left:10px;font-size:5.6px;line-height:7.2px}
.heading{font-weight:600;font-size:6.2px}
.list{list-style:none}
.list li{line-height:8.3px}
.list li::before{content:"-  "}
.indent{padding-left:7px}
.field{position:absolute;left:10px;font-size:5.4px;font-weight:600;display:flex;align-items:flex-end}
.field span{width:50px}
.field i{display:block;width:133px;border-bottom:.6px solid var(--rule)}
.contact{position:absolute;left:20px;font-size:5.4px;line-height:9.6px}
.contact .company{font-weight:600}
.contact p{display:flex;align-items:center;gap:4px}
.seal{position:absolute}
.crop{position:absolute;left:766px;width:426px;background:var(--right-bg);overflow:hidden}
.crop--top{top:0;height:269px;border-radius:0 0 8px 8px;background:linear-gradient(180deg,#fff 35%,var(--blue-mist) 100%)}
.crop--bottom{top:277px;height:269px;border-radius:8px 8px 0 0}
.crop .el{left:7px;font-size:8.3px;line-height:13.4px}
.crop .heading{font-size:10.2px}
.crop .field{left:6px;font-size:7.4px}
.crop .field span{width:68px}
.crop .field i{width:182px}
.crop .contact{left:10px;font-size:7.8px;line-height:13.8px}
.crop--bottom .brand-name{left:16px;top:38px;font-size:48px}
.crop--bottom .el{left:10px;font-size:9px;line-height:13.4px}
.crop--bottom .heading{font-size:10.4px}
</style>
</head>
<body>
<div class="board"></div>

<!-- Front page -->
<section class="sheet sheet--front">
  <svg class="swoosh" width="318" height="80" viewBox="0 0 318 80" aria-hidden="true">
    <path d="M0 0H318V62C250 22 150 6 0 14Z" fill="var(--blue-soft)"/>
    <path d="M150 0C230 8 290 34 318 62V48C282 22 232 6 195 0Z" fill="var(--blue-mid)"/>
    <path d="M225 0C270 10 300 24 318 40V28C300 16 280 6 258 0Z" fill="var(--blue-deep)"/>
  </svg>
  <svg class="fade" width="318" height="90" viewBox="0 0 318 90" aria-hidden="true">
    <path d="M0 40C80 20 200 30 318 10V90H0Z" fill="var(--blue-soft)" opacity=".35"/>
    <path d="M120 90L260 20L318 50V90Z" fill="var(--blue-soft)" opacity=".4"/>
  </svg>
  <div class="brand-name">Slumberwell</div>
  <p class="el heading" style="top:94px;font-weight:500">Congratulations on your new SLUMBERWELL mattress.</p>
  <p class="el" style="top:119px;width:300px">We always strive to provide you with the most comfortable and healthy sleep by offering you the highest product quality and durability.Our company was awarded the ISO 9001 accreditation certificate for the quality of its Mattress Production.By implementing the ISO 9001 quality management system, we assure our customers that the products and the services we provide will meet their expectations.Our products are guaranteed against defects in workmanship and material. In case of defect, we shall repair or replace, at our discretion, the defective component. Please keep this card in a safe place. Should you face any problems, please contact our service department.</p>
  <p class="el heading" style="top:215px">To ensure you get maximum comfort and support, please follow the following instructions:</p>
  <ul class="el list" style="top:231px">
    <li>Make sure the bed base foundation is in good condition and well ventilated.</li>
    <li>Turn/Flip your mattress every 3 months to maximize its comfort and lifespan.</li>
    <li>Avoid exposing the mattress to the sun; air it in a passage area instead.</li>
    <li>In case of possibility of liquids dripping on the mattress, consider covering it with a<br><span class="indent">mattress protection pad.</span></li>
    <li>Do not worry if the mattress feels slightly firmer than anticipated within weeks of usage,<br><span class="indent">the interior will soften and initial stiffness will be removed.</span></li>
  </ul>
  <div class="field" style="top:321px"><span>Invoice Number</span><i></i></div>
  <div class="field" style="top:336px"><span>Warranty Period</span><i></i></div>
  <div class="field" style="top:351px"><span>Date</span><i></i></div>
  <div class="contact" style="top:408px">
    <p class="company">Hadi Rahal and Sons</p>
    <p><svg width="5" height="7" viewBox="0 0 10 14"><path d="M5 0a5 5 0 0 1 5 5c0 4-5 9-5 9S0 9 0 5a5 5 0 0 1 5-5z" fill="var(--blue-deep)"/></svg>Cedar Park, Mill Road, Aley, Lebanon</p>
    <p><svg width="6" height="6" viewBox="0 0 12 12"><path d="M2 0l3 3-1.5 2a8 8 0 0 0 3.5 3.5L9 7l3 3-2 2C5 12 0 7 0 2z" fill="var(--blue-deep)"/></svg>+961 1 555 014</p>
    <p><svg width="6" height="6" viewBox="0 0 12 12"><circle cx="6" cy="6" r="5" fill="none" stroke="var(--blue-deep)" stroke-width="1.6"/></svg>www.hadirahalandsons.com</p>
  </div>
  <svg class="seal" style="left:250px;top:386px" width="56" height="56" viewBox="0 0 56 56" aria-hidden="true"><circle cx="28" cy="28" r="27" fill="var(--seal)"/></svg>
</section>

<!-- Back page -->
<section class="sheet sheet--back">
  <svg class="swoosh" width="318" height="80" viewBox="0 0 318 80" aria-hidden="true">
    <path d="M0 0H318V62C250 22 150 6 0 14Z" fill="var(--blue-soft)"/>
    <path d="M150 0C230 8 290 34 318 62V48C282 22 232 6 195 0Z" fill="var(--blue-mid)"/>
    <path d="M225 0C270 10 300 24 318 40V28C300 16 280 6 258 0Z" fill="var(--blue-deep)"/>
  </svg>
  <svg class="fade" width="318" height="90" viewBox="0 0 318 90" aria-hidden="true">
    <path d="M0 40C80 20 200 30 318 10V90H0Z" fill="var(--blue-soft)" opacity=".35"/>
    <path d="M120 90L260 20L318 50V90Z" fill="var(--blue-soft)" opacity=".4"/>
  </svg>
  <div class="brand-name">Slumberwell</div>
  <p class="el heading" style="top:101px">This limited Mattress Warranty applies to the following Defects:</p>
  <ul class="el list" style="top:120px">
    <li>Coils or wires that are broken or piercing through fabric.</li>
    <li>Sagging, that measures 3cm or greater (being properly measured)<br><span class="indent">only if the mattress has been continuously supported by appropriate and solid foundation</span></li>
  </ul>
  <p class="el heading" style="top:167px">This limited Mattress Warranty does not cover the following:</p>
  <ul class="el list" style="top:187px;line-height:10.4px">
    <li>Comfort preference.</li>
    <li>Fabric Stains, soiling or burns.</li>
    <li>Body impressions of less than 3cm.</li>
    <li>Damage to the mattress due to abuse.</li>
    <li>Bent Perimeter border rods due to moving or bending the mattress</li>
    <li>Size allowance of +/- 2cm.</li>
    <li>Bed Bugs and Dust Mites.</li>
    <li>Mattress Odor: as in any upholstery, new mattress may have odor that will fade with time.</li>
    <li>For Latex and Memory Foam mattresses: normal change in softness and recovery time<br><span class="indent">in these materials with time. This does not affect the relieving qualities of these mattresses.</span></li>
    <li>Transportation and Inspection Costs.</li>
  </ul>
  <div class="contact" style="top:408px">
    <p class="company">Hadi Rahal and Sons</p>
    <p><svg width="5" height="7" viewBox="0 0 10 14"><path d="M5 0a5 5 0 0 1 5 5c0 4-5 9-5 9S0 9 0 5a5 5 0 0 1 5-5z" fill="var(--blue-deep)"/></svg>Cedar Park, Mill Road, Aley, Lebanon</p>
    <p><svg width="6" height="6" viewBox="0 0 12 12"><path d="M2 0l3 3-1.5 2a8 8 0 0 0 3.5 3.5L9 7l3 3-2 2C5 12 0 7 0 2z" fill="var(--blue-deep)"/></svg>+961 1 555 014</p>
    <p><svg width="6" height="6" viewBox="0 0 12 12"><circle cx="6" cy="6" r="5" fill="none" stroke="var(--blue-deep)" stroke-width="1.6"/></svg>www.hadirahalandsons.com</p>
  </div>
  <svg class="seal" style="left:250px;top:386px" width="56" height="56" viewBox="0 0 56 56" aria-hidden="true"><circle cx="28" cy="28" r="27" fill="var(--seal)"/></svg>
</section>

<!-- Detail: front lower half -->
<section class="crop crop--top">
  <svg class="fade" width="426" height="110" viewBox="0 0 426 110" aria-hidden="true">
    <path d="M0 60C120 30 280 40 426 10V110H0Z" fill="var(--blue-soft)" opacity=".3"/>
    <path d="M160 110L340 20L426 60V110Z" fill="var(--blue-soft)" opacity=".35"/>
  </svg>
  <ul class="el list" style="top:6px">
    <li>In case of possibility of liquids dripping on the mattress, consider covering it with a<br><span class="indent">mattress protection pad.</span></li>
    <li>Do not worry if the mattress feels slightly firmer than anticipated within weeks of usage,<br><span class="indent">the interior will soften and initial stiffness will be removed.</span></li>
  </ul>
  <div class="field" style="top:90px"><span>Invoice Number</span><i></i></div>
  <div class="field" style="top:111px"><span>Warranty Period</span><i></i></div>
  <div class="field" style="top:132px"><span>Date</span><i></i></div>
  <div class="contact" style="top:207px">
    <p class="company">Hadi Rahal and Sons</p>
    <p><svg width="7" height="10" viewBox="0 0 10 14"><path d="M5 0a5 5 0 0 1 5 5c0 4-5 9-5 9S0 9 0 5a5 5 0 0 1 5-5z" fill="var(--blue-deep)"/></svg>Cedar Park, Mill Road, Aley, Lebanon</p>
    <p><svg width="8" height="8" viewBox="0 0 12 12"><path d="M2 0l3 3-1.5 2a8 8 0 0 0 3.5 3.5L9 7l3 3-2 2C5 12 0 7 0 2z" fill="var(--blue-deep)"/></svg>+961 1 555 014</p>
    <p><svg width="8" height="8" viewBox="0 0 12 12"><circle cx="6" cy="6" r="5" fill="none" stroke="var(--blue-deep)" stroke-width="1.6"/></svg>www.hadirahalandsons.com</p>
  </div>
  <svg class="seal" style="left:334px;top:182px" width="76" height="76" viewBox="0 0 76 76" aria-hidden="true"><circle cx="38" cy="38" r="37" fill="var(--seal)"/></svg>
</section>

<!-- Detail: back upper half -->
<section class="crop crop--bottom">
  <svg class="swoosh" width="426" height="90" viewBox="0 0 426 90" aria-hidden="true">
    <path d="M0 0H426V80C340 30 200 8 0 14Z" fill="var(--blue-soft)" opacity=".8"/>
    <path d="M150 0C270 10 370 40 426 80V60C370 26 300 8 230 0Z" fill="var(--blue-mid)"/>
    <path d="M270 0C340 10 395 28 426 48V32C400 18 360 6 320 0Z" fill="var(--blue-deep)"/>
  </svg>
  <div class="brand-name">Slumberwell</div>
  <p class="el heading" style="top:139px">This limited Mattress Warranty applies to the following Defects:</p>
  <ul class="el list" style="top:164px">
    <li>Coils or wires that are broken or piercing through fabric.</li>
    <li>Sagging, that measures 3cm or greater (being properly measured)<br><span class="indent">only if the mattress has been continuously supported by appropriate and solid foundation</span></li>
  </ul>
  <p class="el heading" style="top:224px">This limited Mattress Warranty does not cover the following:</p>
  <ul class="el list" style="top:250px">
    <li>Comfort preference.</li>
  </ul>
</section>
</body>
</html>
```